Business Card Design for Kidlarko (Hires out childrens play areas)

Looking to have a business card designed for a company we just bought. The company rents out childrens play areas.

I have uploaded a couple of examples of the kind of business card style I like. Here are two more examples:

https://vesterlingstudio.example.nz/project/brisk-romp-branding/
https://imgvaultcdn.example.com/design_img/8462913/307481/307481_2958174_8462913_a7c3e190_image.jpg

I think a white card will be best due to all the colours in the logo.

Size we require: 3.75" x 2.25" (horizontally orientated) with a 0.125" bleed

Uploaded is two versions of our logo.

Details for the card:
1. My name: Wade Ferrin
2. Title: Managing Director
3. Phone no: 021 537 462
4. Email: wade@kidlarko.example.nz
5. URL: www.kidlarko.example.nz
6. Address:
PO Box 381627
Fernmoor, Auckland

Let me know if you need anything else.

Target Market(s)

Hospitals, doctors surgeries, bed shops, etc.

Contact Information for Business Card

Details for the card:
1. My name: Wade Ferrin
3. Phone no: 021 537 462
5. URL: www.kidlarko.example.nz
6. Address:
PO Box 381627
Fernmoor, Auckland

Requirements
Should not have
• Not too busy.

```html
<!DOCTYPE html>
<html lang="en">
<head>
<meta charset="utf-8">
<title>Kidlarko Business Card</title>
<link rel="stylesheet" href="https://fonts.googleapis.com/css2?family=Roboto:wght@400;500;700&display=swap">
<style>
  :root {
    --page-bg: #ececee;
    --card-white: #ffffff;
    --ink-blue: #2f7fd1;
    --ink-grey: #6b6b70;
    --ink-dark: #4a4a50;
    --brand-purple: #8a2aa8;
    --brand-magenta: #d3179a;
    --back-deep: #5b1f8e;
    --back-glow: #e3129a;
    --stripe-purple: #9b3bb5;
    --stripe-teal: #2bb3b0;
    --stripe-red: #e5343f;
    --stripe-green: #4cb848;
    --stripe-orange: #f5a623;
  }
  * { box-sizing: border-box; margin: 0; padding: 0; }
  html, body {
    width: 1200px; height: 950px; overflow: hidden;
    background: var(--page-bg);
    font-family: "Roboto", Arial, sans-serif;
  }
  .canvas {
    position: relative; width: 1200px; height: 950px;
  }
  .card {
    position: absolute; left: 300px; width: 600px; height: 360px;
    border-radius: 4px;
    box-shadow: 0 6px 18px rgba(0,0,0,0.15);
    overflow: hidden;
  }
  .card-front { top: 80px; background: var(--card-white); }
  .card-back {
    top: 510px;
    background: radial-gradient(ellipse at 45% 50%, var(--back-glow) 0%, #b1169a 35%, var(--back-deep) 85%);
  }

  .brand-mark {
    position: absolute; display: flex; align-items: center; gap: 10px;
  }
  .brand-mark .dot { border-radius: 50%; flex: none; }
  .brand-mark .name { font-weight: 700; letter-spacing: 0.5px; }

  .card-front .brand-mark { top: 46px; right: 48px; }
  .card-front .brand-mark .dot { width: 40px; height: 40px; background: var(--brand-magenta); }
  .card-front .brand-mark .name { font-size: 30px; color: var(--brand-purple); }

  .card-back .brand-mark { top: 50%; left: 50%; transform: translate(-50%, -50%); }
  .card-back .brand-mark .dot { width: 52px; height: 52px; background: #ffffff; }
  .card-back .brand-mark .name { font-size: 46px; color: #ffffff; }

  .holder { position: absolute; left: 44px; top: 166px; }
  .holder .person {
    font-size: 22px; font-weight: 700; color: var(--ink-blue);
    text-transform: uppercase; letter-spacing: 0.3px;
  }
  .holder .role {
    margin-top: 3px; font-size: 14px; color: var(--ink-grey);
    text-transform: uppercase; letter-spacing: 0.6px;
  }

  .stripe {
    position: absolute; left: 44px; right: 44px; top: 226px; height: 3px;
    display: flex;
  }
  .stripe span { flex: 1; }
  .stripe .s1 { background: var(--stripe-purple); }
  .stripe .s2 { background: var(--stripe-teal); }
  .stripe .s3 { background: var(--stripe-red); }
  .stripe .s4 { background: var(--stripe-green); }
  .stripe .s5 { background: var(--stripe-orange); }

  .contact-list {
    position: absolute; left: 44px; top: 244px; list-style: none;
    font-size: 13.5px; color: var(--ink-grey); line-height: 22px;
  }
  .contact-list li { display: flex; align-items: center; gap: 9px; }
  .contact-list svg { width: 12px; height: 12px; fill: var(--ink-dark); flex: none; }

  .postal {
    position: absolute; right: 44px; top: 244px; text-align: right;
    font-size: 14px; color: var(--ink-grey); line-height: 22px;
  }
</style>
</head>
<body>
<main class="canvas">
  <section class="card card-front" aria-label="Business card front">
    <div class="brand-mark">
      <span class="dot"></span>
      <span class="name">Kidlarko</span>
    </div>

    <div class="holder">
      <p class="person">Wade Ferrin</p>
      <p class="role">Managing Director</p>
    </div>

    <div class="stripe">
      <span class="s1"></span><span class="s2"></span><span class="s3"></span><span class="s4"></span><span class="s5"></span>
    </div>

    <ul class="contact-list">
      <li>
        <svg viewBox="0 0 24 24" aria-hidden="true"><path d="M6.6 10.8a15.1 15.1 0 0 0 6.6 6.6l2.2-2.2c.3-.3.7-.4 1-.2 1.1.4 2.3.6 3.6.6.6 0 1 .4 1 1V20c0 .6-.4 1-1 1A17 17 0 0 1 3 4c0-.6.4-1 1-1h3.5c.6 0 1 .4 1 1 0 1.3.2 2.5.6 3.6.1.3 0 .7-.2 1z"/></svg>
        <span>021 537 462</span>
      </li>
      <li>
        <svg viewBox="0 0 24 24" aria-hidden="true"><path d="M2 5h20v14H2zm2 2v.4l8 5 8-5V7zm0 2.8V17h16V9.8l-8 5z"/></svg>
        <span>wade@kidlarko.example.nz</span>
      </li>
      <li>
        <svg viewBox="0 0 24 24" aria-hidden="true"><path d="M12 2a10 10 0 1 0 0 20 10 10 0 0 0 0-20zm6.9 6h-3a15 15 0 0 0-1.3-4 8 8 0 0 1 4.3 4zM12 4c.8 1.2 1.5 2.5 1.9 4h-3.8c.4-1.5 1.1-2.8 1.9-4zM4.3 14a8 8 0 0 1 0-4h3.4a16 16 0 0 0 0 4zm.8 2h3a15 15 0 0 0 1.3 4 8 8 0 0 1-4.3-4zm3-8h-3a8 8 0 0 1 4.3-4 15 15 0 0 0-1.3 4zM12 20c-.8-1.2-1.5-2.5-1.9-4h3.8c-.4 1.5-1.1 2.8-1.9 4zm2.3-6H9.7a14 14 0 0 1 0-4h4.6a14 14 0 0 1 0 4zm.3 6a15 15 0 0 0 1.3-4h3a8 8 0 0 1-4.3 4zm1.7-6a16 16 0 0 0 0-4h3.4a8 8 0 0 1 0 4z"/></svg>
        <span>www.kidlarko.example.nz</span>
      </li>
    </ul>

    <address class="postal" style="font-style: normal;">
      PO Box 381627<br>
      Fernmoor, Auckland
    </address>
  </section>

  <section class="card card-back" aria-label="Business card back">
    <div class="brand-mark">
      <span class="dot"></span>
      <span class="name">Kidlarko</span>
    </div>
  </section>
</main>
</body>
</html>
```